Oakleaf medical

We are a doctors surgery, providing medical services to all ages

we aim for a professional as well as an eye catching look for the signs that can be seen by passing vehicles and people who walk by

trustworthy quality medical care to to all patients, we treat like family

Name- Brookmere Oakleaf Medical practice

Target Market(s)

all ages, adults
the elderly

Industry/Entity Type

Medical

Requirements
Must have
• eye catching,
obvious medical service location

```html
<!DOCTYPE html>
<html lang="en">
<head>
<meta charset="utf-8">
<title>Brookmere Oakleaf Medical Practice – Sign</title>
<link rel="stylesheet" href="https://fonts.googleapis.com/css2?family=Cinzel:wght@700;900&family=Mulish:wght@800&family=Open+Sans:wght@800&display=swap">
<style>
  :root {
    --page: #ffffff;
    --gold-light: #f7d45a;
    --gold-mid: #e4b33a;
    --gold-dark: #c98f26;
    --title-blue: #1f3a9c;
    --title-green: #3aa23c;
    --ring-blue: #1b8fd6;
    --ring-green: #5cb84a;
    --pill-light: #f77bbf;
    --pill-dark: #e0267f;
    --tagline: #2a1c6e;
    --photo-a: #f1dcc9;
    --photo-b: #b9d3ea;
  }
  * { margin: 0; padding: 0; box-sizing: border-box; }
  html, body {
    width: 1200px; height: 772px; overflow: hidden; background: var(--page);
  }
  .sign {
    position: absolute; left: 36px; top: 235px; width: 1128px; height: 301px;
    background: var(--page);
  }
  .sign__bands { position: absolute; inset: 0; }
  .brand-mark {
    position: absolute; left: 16px; top: 45px; width: 164px; height: 164px;
    border-radius: 50%; border: 7px solid var(--ring-blue);
    display: flex; align-items: center; justify-content: center; text-align: center;
  }
  .brand-mark__name {
    font-family: "Cinzel", serif; font-weight: 700; font-size: 19px; line-height: 1.2;
    color: var(--title-blue);
  }
  .title {
    position: absolute; left: 196px; top: 38px; width: 614px; text-align: center;
    font-family: "Cinzel", serif; font-weight: 900; line-height: 1;
  }
  .title__name { display: block; font-size: 43px; color: var(--title-blue); letter-spacing: 0.5px; }
  .title__type { display: block; font-size: 51px; color: var(--title-green); margin-top: 12px; }
  .phone {
    position: absolute; left: 289px; top: 185px; width: 428px; height: 48px;
    border-radius: 24px;
    background: linear-gradient(to bottom, var(--pill-light), var(--pill-dark) 60%, var(--pill-light));
    display: flex; align-items: center; justify-content: center; gap: 18px;
    color: #fff; font-family: "Open Sans", sans-serif; font-weight: 800; font-size: 36px;
    letter-spacing: 1px;
  }
  .phone__icon { width: 38px; height: 30px; }
  .photo {
    position: absolute; left: 778px; top: 30px; width: 350px; height: 218px;
    background: linear-gradient(120deg, var(--photo-a), var(--photo-b));
  }
  .tagline {
    position: absolute; left: 0; top: 256px; width: 1128px; text-align: center;
    font-family: "Mulish", sans-serif; font-weight: 800; font-size: 31px;
    color: var(--tagline); letter-spacing: 1.2px;
  }
</style>
</head>
<body>
  <div class="sign">
    <svg class="sign__bands" width="1128" height="301" viewBox="0 0 1128 301" aria-hidden="true">
      <defs>
        <linearGradient id="goldFill" x1="0" y1="0" x2="0" y2="1">
          <stop offset="0" stop-color="var(--gold-mid)"/>
          <stop offset="0.5" stop-color="var(--gold-light)"/>
          <stop offset="1" stop-color="var(--gold-dark)"/>
        </linearGradient>
      </defs>
      <path d="M0 0 H1128 V8 Q700 20 400 26 Q150 28 0 30 Z" fill="url(#goldFill)"/>
      <path d="M0 245 Q300 238 600 244 Q900 252 1128 236 V301 H0 Z" fill="url(#goldFill)"/>
    </svg>

    <div class="brand-mark">
      <span class="brand-mark__name">Oakleaf<br>medical</span>
    </div>

    <h1 class="title">
      <span class="title__name">Brookmere Oakleaf</span>
      <span class="title__type">Medical Practice</span>
    </h1>

    <div class="phone">
      <svg class="phone__icon" viewBox="0 0 38 30" aria-hidden="true">
        <path d="M2 9 Q19 -2 36 9 L33 13 L26 11 L25 7 Q19 5 13 7 L12 11 L5 13 Z" fill="#fff"/>
        <path d="M9 14 H29 L34 28 H4 Z" fill="#fff"/>
        <circle cx="19" cy="21" r="4" fill="var(--pill-dark)"/>
      </svg>
      <span class="phone__number">9180 4432</span>
    </div>

    <div class="photo" role="img" aria-label="Photo of a smiling female doctor with a stethoscope beside a happy multi-generation family"></div>

    <p class="tagline">Trustworthy medical care for all patients</p>
  </div>
</body>
</html>
```